Business card design for online Mandarin Learning School

We need a business card design for our online language learning school called "Maple Bridge Online for Mandarin Learning". Our existing website is https://www.maplebridgeonline.com
We have our logo already. We would like to see our business card design that can make our online teaching services to be innovative, young, energetic and fun to learn. Prefer to have a certain level of color matching with our website. Apart from "Maple Bridge Online", need to specifically state "for Mandarin Learning" as well on the business card.

```html
<!DOCTYPE html>
<html lang="en">
<head>
<meta charset="utf-8">
<title>Maple Bridge Online for Mandarin Learning – Business Card</title>
<link rel="stylesheet" href="https://fonts.googleapis.com/css2?family=Cinzel:wght@400;500&family=Lato:wght@400&display=swap">
<style>
  :root {
    --page: #d9d9dc;
    --coral: #e25f5c;
    --teal: #13aebb;
    --slate: #8a8a8c;
    --cream: #f2f1e7;
    --ink: #2b2b2b;
    --rule: #c9c8be;
  }
  * { box-sizing: border-box; margin: 0; padding: 0; }
  html, body { width: 1200px; height: 900px; overflow: hidden; }
  body {
    background: var(--page);
    position: relative;
    font-family: "Lato", Arial, sans-serif;
  }
  .card {
    position: absolute;
    width: 525px;
    height: 300px;
    border-radius: 26px;
    overflow: hidden;
    box-shadow: 0 10px 24px rgba(0,0,0,0.18);
  }

  /* Front */
  .card-front {
    left: 70px;
    top: 110px;
    background: linear-gradient(168deg, var(--slate) 0%, var(--coral) 38%, var(--coral) 58%, var(--teal) 100%);
    display: flex;
    flex-direction: column;
    align-items: center;
    justify-content: center;
    color: #fff;
    font-family: "Cinzel", "Times New Roman", serif;
    text-align: center;
    line-height: 1.15;
  }
  .front-name { font-size: 34px; letter-spacing: 1px; }
  .front-tag { font-size: 21px; font-weight: 500; letter-spacing: 1px; }

  /* Back */
  .card-back {
    left: 605px;
    top: 470px;
    background: var(--cream);
  }
  .brand {
    position: absolute;
    right: 34px;
    top: 40px;
    display: flex;
    align-items: center;
    gap: 12px;
  }
  .brand-dot {
    width: 26px; height: 26px;
    border-radius: 50%;
    background: var(--coral);
  }
  .brand-name {
    font-family: "Cinzel", "Times New Roman", serif;
    font-size: 30px;
    color: var(--teal);
    letter-spacing: 1px;
  }
  .divider {
    position: absolute;
    left: 34px; right: 34px;
    top: 112px;
    height: 1px;
    background: var(--rule);
  }
  .edge-coral {
    position: absolute;
    right: 0; top: 98px;
    width: 22px; height: 28px;
    background: var(--coral);
  }
  .address {
    position: absolute;
    right: 34px; top: 126px;
    text-align: right;
    font-size: 14px;
    color: var(--ink);
    line-height: 1.3;
  }
  .person {
    position: absolute;
    left: 34px; top: 178px;
  }
  .person-name {
    font-family: "Cinzel", "Times New Roman", serif;
    font-size: 22px;
    letter-spacing: 1px;
    color: var(--teal);
  }
  .person-name .surname { color: var(--slate); }
  .person-role { font-size: 14px; color: var(--ink); margin-top: 1px; }
  .contacts { list-style: none; margin-top: 6px; }
  .contacts li {
    display: flex; align-items: center; gap: 7px;
    font-size: 14.5px; color: var(--ink); line-height: 1.35;
  }
  .contacts svg { width: 12px; height: 12px; fill: var(--teal); flex: none; }
  .edge-teal {
    position: absolute; left: 0; top: 200px;
    width: 22px; height: 30px; background: var(--teal);
  }
  .edge-slate {
    position: absolute; left: 0; top: 236px;
    width: 22px; height: 40px; background: var(--slate);
  }
</style>
</head>
<body>
  <section class="card card-front" aria-label="Business card front">
    <p class="front-name">Maple Bridge</p>
    <p class="front-tag">Online for</p>
    <p class="front-tag">Mandarin Learning</p>
  </section>

  <section class="card card-back" aria-label="Business card back">
    <div class="brand">
      <span class="brand-dot"></span>
      <span class="brand-name">Maple Bridge</span>
    </div>
    <div class="divider"></div>
    <div class="edge-coral"></div>
    <p class="address">17 Harbour Lane<br>Springvale, 30418</p>

    <div class="edge-teal"></div>
    <div class="edge-slate"></div>
    <div class="person">
      <p class="person-name">Daniel <span class="surname">Hart</span></p>
      <p class="person-role">Managing Director</p>
      <ul class="contacts">
        <li>
          <svg viewBox="0 0 24 24" aria-hidden="true"><path d="M6.6 10.8a15.1 15.1 0 0 0 6.6 6.6l2.2-2.2a1 1 0 0 1 1-.25 11.4 11.4 0 0 0 3.6.57 1 1 0 0 1 1 1V20a1 1 0 0 1-1 1A17 17 0 0 1 3 4a1 1 0 0 1 1-1h3.5a1 1 0 0 1 1 1c0 1.25.2 2.45.57 3.6a1 1 0 0 1-.25 1z"/></svg>
          044-555 010 200
        </li>
        <li>
          <svg viewBox="0 0 24 24" aria-hidden="true"><path d="M2 5h20v14H2z M2 5l10 8 10-8" /></svg>
          hello@maplebridgeonline.com
        </li>
        <li>
          <svg viewBox="0 0 24 24" aria-hidden="true"><circle cx="12" cy="12" r="10"/></svg>
          www.maplebridgeonline.com
        </li>
      </ul>
    </div>
  </section>
</body>
</html>
```